Velvane Detailing – Premium Automotive Detailing Studio Website Design

We're launching a premium automotive detailing studio called Velvane Detailing, and we’re looking for a clean, minimal, and high-end website design (desktop + mobile version). The studio targets owners of luxury vehicles who care deeply about aesthetics, perfection, and exceptional service.
This project is about more than just showing services , it should feel like a luxury experience from the very first second. The design should be modern, minimalistic, elegant, and clearly aimed at an upscale market.
We’re looking for a designer who can translate our physical studio’s premium interior and architectural feel into a digital presence.
What we want the website to feel like:
Clean and modern
Professional and luxurious
Minimal and not cluttered
Light animations or transitions to add polish
Stylish and cinematic
Design freedom:
We trust your design direction. We are not providing strict color codes or layout instructions, we want you to create what you believe works best based on our brand positioning and target audience. Just keep it premium, modern, and well-organized.
What the website should include:
Hero section with a bold visual (image or video)
About the Studio — a few blocks explaining our story and focus on quality
Service Overview — clearly showing what we offer (detailing, ceramic coating, interior, etc.)
Gallery/Showcase — show off our work with cars, interior, and the space itself
Client Lounge Area — mention comfort, coffee, and waiting space
Testimonials — social proof from satisfied clients
Location & contact section — map, address, contact form
Footer, simple with nav, contact info, and optional social media
Target audience:
Owners of high-end vehicles (Torvana, Kalvex, etc.)
Car collectors and detailing enthusiasts
People looking for premium-level service and presentation
Brands/creators booking our photo studio

```html
<!DOCTYPE html>
<html lang="en">
<head>
<meta charset="utf-8">
<title>Velvane Detailing</title>
<link href="https://fonts.googleapis.com/css2?family=Michroma&family=Montserrat:wght@400;500;600;700&display=swap" rel="stylesheet">
<style>
:root{
  --black:#000;
  --ink:#0b0b0b;
  --graphite:#1b1b1d;
  --gold:#e0b43c;
  --gold-deep:#b8862a;
  --gold-soft:#f1d27a;
  --white:#fff;
  --grey:#bdbdbd;
  --display:'Michroma',sans-serif;
  --body:'Montserrat',sans-serif;
}
*{margin:0;padding:0;box-sizing:border-box}
html,body{width:1200px;height:5310px;overflow:hidden;background:var(--black);color:var(--white);font-family:var(--body)}
.page{position:relative;width:1200px;height:5310px}
.abs{position:absolute}
.ph{position:absolute}
.gold{color:var(--gold)}
.display{font-family:var(--display);text-transform:uppercase;letter-spacing:2px}
.btn{position:absolute;display:flex;align-items:center;justify-content:center;border:1.5px solid var(--gold);font-size:12px;font-weight:700;letter-spacing:2px;color:var(--white)}
.btn::after{content:"";position:absolute;right:-8px;top:50%;width:14px;height:14px;border-top:3px solid var(--gold);border-right:3px solid var(--gold);transform:translateY(-50%) rotate(45deg)}
.sec-title{position:absolute;left:0;width:1200px;text-align:center;font-family:var(--display);font-size:34px;letter-spacing:3px;text-transform:uppercase}
.sec-title::after{content:"";display:block;width:60px;height:3px;background:var(--grey);margin:18px auto 0}
.sec-mark{position:absolute;left:588px;width:24px;height:24px;border:3px solid var(--white)}
.arrow{position:absolute;width:40px;height:40px;border:2px solid var(--gold);border-radius:50%}
.arrow svg{width:100%;height:100%}

/* nav */
.nav{position:absolute;top:0;left:0;width:1200px;height:90px;z-index:3}
.brand{position:absolute;left:128px;top:28px;display:flex;align-items:center;gap:10px;font-size:17px;font-weight:700;letter-spacing:3px;color:var(--white)}
.brand i{width:18px;height:18px;background:var(--white);display:block}
.nav a{position:absolute;top:40px;font-size:12px;font-weight:700;letter-spacing:1px;color:var(--white);text-decoration:none}
.nav .active::after{content:"";position:absolute;left:0;right:0;bottom:-9px;height:2px;background:var(--white)}
.nav .sep{position:absolute;top:40px;width:1px;height:14px;background:#666}
.nav .contact{left:993px;top:30px;width:125px;height:36px;border:1.5px solid var(--white);display:flex;align-items:center;justify-content:center}

/* hero */
.hero-h{left:122px;top:180px;font-family:var(--display);font-size:41px;line-height:50px;letter-spacing:2px}
.hero-sub{left:122px;top:345px;font-size:20px;letter-spacing:1px}

/* about */
.about-text{left:645px;top:838px;width:470px;font-size:16px;line-height:27px;color:#eaeaea}
.about-text p+p{margin-top:26px}

/* services */
.svc-label{position:absolute;font-family:var(--display);font-size:18px;letter-spacing:2px;text-align:center}

/* lounge */
.lounge-title{left:145px;top:2045px;font-family:var(--display);font-size:33px;line-height:42px;letter-spacing:3px}
.lounge-intro{left:628px;top:2040px;width:420px;font-size:15.5px;line-height:27px}
.perk{position:absolute;left:632px;width:440px;display:flex;gap:22px}
.perk h4{font-size:16px;font-weight:700;letter-spacing:.5px}
.perk p{font-size:12.5px;line-height:16px;margin-top:2px}
.perk svg{flex:none;width:52px;height:52px}

/* testimonial */
.quote-box{left:300px;top:3524px;width:596px;height:281px;border:2px solid var(--gold);text-align:center;padding-top:40px}
.stars{color:var(--gold);font-size:28px;letter-spacing:4px}
.quote{font-size:19.5px;line-height:30px;margin:14px 40px 0}
.author{font-size:21px;font-weight:700;margin-top:10px}

/* contact */
.contact-title{left:137px;top:4430px;font-family:var(--display);font-size:34px;letter-spacing:3px}
.contact-sub{left:137px;top:4500px;font-size:15.5px;color:#ddd}
.c-item{position:absolute;left:136px;display:flex;gap:18px;font-size:17px;line-height:28px}
.c-ico{flex:none;width:50px;height:50px;border-radius:50%;background:var(--gold);display:flex;align-items:center;justify-content:center}
.c-ico svg{width:24px;height:24px}
.form{left:608px;top:4418px;width:507px;height:408px;background:linear-gradient(120deg,#b88a2f,#e9c86a 45%,#c99a3c)}
.field{position:absolute;border:1.5px solid #7d5a1a;font-size:13px;color:#222;padding:12px 24px}
.submit{position:absolute;left:52px;top:326px;width:168px;height:40px;background:var(--black);color:var(--white);font-size:12px;font-weight:700;letter-spacing:2px;display:flex;align-items:center;justify-content:center}

/* footer */
.f-brand{left:0;width:1200px;top:5010px;text-align:center;font-size:22px;font-weight:700;letter-spacing:4px}
.f-nav{left:140px;top:5080px;width:920px;display:flex;justify-content:space-between;align-items:center;font-size:13.5px;font-weight:700;letter-spacing:1px}
.f-nav b{width:5px;height:5px;border-radius:50%;background:var(--gold)}
.f-line{height:1px;background:#333}
.f-item{position:absolute;top:5140px;display:flex;gap:14px;align-items:center;font-size:13.5px;line-height:19px}
.f-item .c-ico{width:42px;height:42px}
.copy{left:0;width:1200px;top:5278px;text-align:center;font-size:11px;color:#888}
</style>
</head>
<body>
<div class="page">

  <!-- HERO -->
  <div class="ph" style="left:0;top:0;width:1200px;height:700px;background:linear-gradient(90deg,#050505 0%,#0d0d0d 40%,#4a4a4c 70%,#8d8e90 88%,#b5b6b8 100%)" role="img" aria-label="Close-up of a polishing machine buffing the headlight of a white luxury car"></div>
  <svg class="abs" style="left:0;top:560px" width="1200" height="150" viewBox="0 0 1200 150">
    <polygon points="0,60 600,112 1200,60 1200,150 0,150" fill="#000"/>
    <polyline points="0,60 600,112 1200,60" fill="none" stroke="var(--gold)" stroke-width="2"/>
  </svg>

  <nav class="nav">
    <div class="brand"><i></i>VELVANE DETAILING</div>
    <a class="active" style="left:408px">HOME</a><span class="sep" style="left:472px"></span>
    <a style="left:496px">ABOUT US</a><span class="sep" style="left:590px"></span>
    <a style="left:614px">SERVICES</a><span class="sep" style="left:704px"></span>
    <a style="left:728px">GALLERY</a><span class="sep" style="left:812px"></span>
    <a style="left:836px">CLIENT LONGE</a>
    <a class="contact">CONTACT</a>
  </nav>

  <h1 class="abs hero-h"><span class="gold">PREMIUM<br>DETAILING</span> FOR<br>LUXURY VEHICLES</h1>
  <p class="abs hero-sub">WHERE PRECISION MEETS PERFECTION</p>
  <div class="btn" style="left:128px;top:396px;width:192px;height:44px">EXPLORE SERVICE</div>

  <!-- ABOUT -->
  <div class="sec-mark" style="top:660px"></div>
  <h2 class="sec-title" style="top:712px">About the <span class="gold">Studio</span></h2>
  <div class="ph" style="left:120px;top:840px;width:460px;height:370px;background:linear-gradient(135deg,#1c1c1c,#6a6a6a 50%,#141414)" role="img" aria-label="Black and white collage of detailing work on a luxury car"></div>
  <div class="abs about-text">
    <p>Velvane Detailing is more than a studio — it's a sanctuary for automotive excellence. Designed to reflect modern luxury, every element of our space and process is tailored to perfectionists.</p>
    <p>Lorem ipsum dolor sit amet, consectetur adipiscing elit, sed do eiusmod tempor incididunt ut labore et dolore magna aliqua. Quis ipsum suspendisse ultrices gravida. Risus commodo viverra maecenas accumsan lacus vel facilisis.</p>
  </div>
  <div class="btn" style="left:650px;top:1153px;width:182px;height:46px">LEARN MORE</div>

  <!-- SERVICES -->
  <svg class="abs" style="left:0;top:1150px" width="1200" height="800" viewBox="0 0 1200 800">
    <polygon points="0,0 600,110 1200,0 1200,800 0,800" fill="var(--graphite)"/>
    <polygon points="0,0 600,110 1200,0 1200,0 0,0" fill="#000"/>
  </svg>
  <div class="sec-mark" style="top:1350px"></div>
  <h2 class="sec-title" style="top:1400px">Our Services</h2>
  <svg class="abs" style="left:0;top:1440px" width="1200" height="440" viewBox="0 0 1200 440">
    <polygon points="272,40 440,208 272,376 104,208" fill="#3a3a3c" role="img" aria-label="Technician polishing a car body"/>
    <polygon points="948,40 1132,224 948,410 764,224" fill="#6d5a45" role="img" aria-label="Luxury car interior with tan leather seats"/>
    <polygon points="612,35 800,226 612,416 422,226" fill="#0c0c0c" stroke="var(--gold)" stroke-width="2"/>
  </svg>
  <div class="svc-label" style="left:172px;top:1740px;width:200px">DETAILING</div>
  <div class="svc-label" style="left:848px;top:1746px;width:200px">INTERIOR</div>
  <div class="svc-label" style="left:462px;top:1602px;width:300px">CERAMIC COATING</div>
  <p class="abs" style="left:492px;top:1636px;width:240px;font-size:11.5px;line-height:17px;text-align:center">Lorem ipsum dolor sit amet, consectetur adipiscing elit sed do Lorem ipsum dolor sit amet, consectetur</p>
  <div class="abs" style="left:543px;top:1706px;width:140px;height:36px;border:1.5px solid var(--gold);display:flex;align-items:center;justify-content:center;font-size:10.5px;font-weight:700;letter-spacing:2px">LEARN MORE</div>
  <div class="arrow" style="left:555px;top:1878px"><svg viewBox="0 0 40 40"><polyline points="23,13 16,20 23,27" fill="none" stroke="#fff" stroke-width="2"/></svg></div>
  <div class="arrow" style="left:612px;top:1878px"><svg viewBox="0 0 40 40"><polyline points="17,13 24,20 17,27" fill="none" stroke="#fff" stroke-width="2"/></svg></div>

  <!-- CLIENT LOUNGE -->
  <div class="ph" style="left:0;top:1950px;width:1200px;height:590px;background:var(--black)"></div>
  <div class="ph" style="left:0;top:2010px;width:700px;height:530px;background:linear-gradient(100deg,#6b5a47,#3b342d 55%,#0a0a0a)" role="img" aria-label="Client lounge with wooden slat walls and cream armchairs"></div>
  <h2 class="abs lounge-title">CLIENT<br>LOUNGE <span class="gold">AREA</span></h2>
  <p class="abs lounge-intro">Luxury isn't just for your car. it's for you. Relax in our premium client lounge with artisanal coffee, curated magazines, and ambient comfort.</p>
  <div class="perk" style="top:2180px">
    <svg viewBox="0 0 52 52" fill="none" stroke="var(--gold)" stroke-width="2"><path d="M10 22v-8q0-4 4-4h24q4 0 4 4v8"/><path d="M6 22h8v10h24V22h8v14H6z"/><path d="M10 36v5M42 36v5"/></svg>
    <div><h4>COMFORT</h4><p>Lorem ipsum dolor sit amet, consectetur adipiscing elit, sed do eiusmod tempor incididun</p></div>
  </div>
  <div class="perk" style="top:2272px">
    <svg viewBox="0 0 52 52" fill="none" stroke="var(--gold)" stroke-width="2"><path d="M10 22h26v10q0 8-8 8h-10q-8 0-8-8z"/><path d="M36 25h4q4 0 4 4t-4 4h-4"/><path d="M6 44h40"/><path d="M18 8q-3 4 0 8M24 6q-3 5 0 10"/></svg>
    <div><h4>COFFEE</h4><p>Lorem ipsum dolor sit amet, consectetur adipiscing elit, sed do eiusmod tempor incididun</p></div>
  </div>
  <div class="perk" style="top:2366px">
    <svg viewBox="0 0 52 52" fill="none" stroke="var(--gold)" stroke-width="2"><circle cx="16" cy="16" r="10"/><path d="M16 10v6l4 3"/><path d="M22 34h24v6H22zM26 34v-8h16v8M24 40v6M44 40v6"/></svg>
    <div><h4>WAITING SPACE</h4><p>Lorem ipsum dolor sit amet, consectetur adipiscing elit, sed do eiusmod tempor incididun</p></div>
  </div>

  <!-- GALLERY -->
  <div class="ph" style="left:0;top:2540px;width:1200px;height:805px;background:radial-gradient(ellipse at 50% 40%,#262628,#0c0c0c 75%)"></div>
  <div class="sec-mark" style="top:2588px"></div>
  <h2 class="sec-title" style="top:2640px">Our <span class="gold">Gallery</span></h2>
  <div class="ph" style="left:105px;top:2725px;width:322px;height:210px;background:linear-gradient(135deg,#2a2a2a,#d4511c 55%,#8a2a0e)" role="img" aria-label="Orange sports car being detailed"></div>
  <div class="ph" style="left:440px;top:2725px;width:322px;height:210px;background:linear-gradient(135deg,#1a1a1a,#8a8a8a 60%,#e8e8e8)" role="img" aria-label="Car dashboard and steering wheel"></div>
  <div class="ph" style="left:775px;top:2725px;width:322px;height:210px;background:linear-gradient(135deg,#0a0f2a,#1e3aa8 55%,#0a1540)" role="img" aria-label="Blue car headlight being polished"></div>
  <div class="ph" style="left:107px;top:2950px;width:486px;height:265px;background:linear-gradient(160deg,#5a4a3a,#a8a8aa 55%,#3a3530)" role="img" aria-label="Silver SUV parked in the studio"></div>
  <div class="ph" style="left:605px;top:2950px;width:487px;height:265px;background:linear-gradient(160deg,#3a3f47,#b0161c 55%,#25282e)" role="img" aria-label="Red Torvana sedan parked outdoors"></div>
  <div class="arrow" style="left:547px;top:3238px"><svg viewBox="0 0 40 40"><polyline points="23,13 16,20 23,27" fill="none" stroke="#fff" stroke-width="2"/></svg></div>
  <div class="arrow" style="left:605px;top:3238px"><svg viewBox="0 0 40 40"><polyline points="17,13 24,20 17,27" fill="none" stroke="#fff" stroke-width="2"/></svg></div>

  <!-- TESTIMONIALS -->
  <div class="sec-mark" style="top:3392px"></div>
  <h2 class="sec-title" style="top:3440px">Testimonials</h2>
  <div class="abs quote-box">
    <div class="stars">★★★★★</div>
    <p class="quote">Lorem ipsum dolor sit amet consectetur adipiscing elit, sed do eiusmod tempor incididunt ut labore et dolore magna aliqua Quis ipsum suspendisse ultrices gravida Risus commodo viverra</p>
    <p class="author">Marcus Hale</p>
  </div>
  <svg class="abs" style="left:130px;top:3640px" width="30" height="44" viewBox="0 0 30 44"><polyline points="24,2 4,22 24,42" fill="none" stroke="#fff" stroke-width="2.5"/></svg>
  <svg class="abs" style="left:1060px;top:3640px" width="30" height="44" viewBox="0 0 30 44"><polyline points="6,2 26,22 6,42" fill="none" stroke="#fff" stroke-width="2.5"/></svg>

  <!-- MAP -->
  <div class="ph" style="left:0;top:3912px;width:1200px;height:408px;background:linear-gradient(180deg,#2a2a2c,#202022)" role="img" aria-label="Dark street map showing the studio location in the city"></div>
  <div class="abs" style="left:568px;top:4084px;width:48px;height:48px;border-radius:50%;background:var(--gold);border:3px solid #fff"></div>

  <!-- CONTACT -->
  <h2 class="abs contact-title">CONTACT US</h2>
  <p class="abs contact-sub">Lorem ipsum dolor sit amet consectetur adipiscing</p>
  <div class="c-item" style="top:4560px">
    <div class="c-ico"><svg viewBox="0 0 24 24"><path d="M12 2a7 7 0 0 0-7 7c0 5 7 13 7 13s7-8 7-13a7 7 0 0 0-7-7z" fill="#000"/><circle cx="12" cy="9" r="2.5" fill="var(--gold)"/></svg></div>
    <div><b>Velvane Detailing</b><br>218 Harbor Lane Suite 400<br>Eastport, NY 10094, United State</div>
  </div>
  <div class="c-item" style="top:4660px;align-items:center">
    <div class="c-ico"><svg viewBox="0 0 24 24"><path d="M6 3l3 0 2 5-2 1.5a11 11 0 0 0 5.5 5.5L16 13l5 2v3a2 2 0 0 1-2 2A16 16 0 0 1 4 5a2 2 0 0 1 2-2z" fill="#000"/></svg></div>
    <div>(+555) 014 2290</div>
  </div>
  <div class="c-item" style="top:4726px;align-items:center">
    <div class="c-ico"><svg viewBox="0 0 24 24"><rect x="3" y="6" width="18" height="12" rx="1" fill="#000"/><polyline points="3,7 12,13 21,7" fill="none" stroke="var(--gold)" stroke-width="1.5"/></svg></div>
    <div>enquiry@velvanedetailing.com</div>
  </div>

  <form class="abs form">
    <div class="field" style="left:52px;top:40px;width:200px;height:48px">First Name</div>
    <div class="field" style="left:262px;top:40px;width:202px;height:48px">Last Name</div>
    <div class="field" style="left:52px;top:102px;width:412px;height:48px">Email address</div>
    <div class="field" style="left:52px;top:164px;width:412px;height:48px">Phone Number</div>
    <div class="field" style="left:52px;top:226px;width:412px;height:84px">Message</div>
    <div class="submit">BOOK NOW</div>
  </form>

  <!-- FOOTER -->
  <svg class="abs" style="left:0;top:4900px" width="1200" height="40" viewBox="0 0 1200 40">
    <path d="M120 38 Q600 -10 1080 38" fill="none" stroke="var(--gold)" stroke-width="3"/>
  </svg>
  <div class="abs" style="left:586px;top:4960px;width:28px;height:28px;background:var(--white)"></div>
  <div class="abs f-brand">VELVANE DETAILING</div>
  <div class="abs f-line" style="left:140px;top:5060px;width:920px"></div>
  <div class="abs f-nav"><span>HOME</span><b></b><span>ABOUT US</span><b></b><span>SERVICES</span><b></b><span>GALLERY</span><b></b><span>CLIENT LONGE</span><b></b><span>TESTIMONIALS</span><b></b><span>CONTACT</span></div>
  <div class="abs f-line" style="left:140px;top:5120px;width:920px"></div>
  <div class="f-item" style="left:168px">
    <div class="c-ico"><svg viewBox="0 0 24 24"><path d="M12 2a7 7 0 0 0-7 7c0 5 7 13 7 13s7-8 7-13a7 7 0 0 0-7-7z" fill="#000"/><circle cx="12" cy="9" r="2.5" fill="var(--gold)"/></svg></div>
    <div>218 Harbor Lane Suite 400<br>Eastport, NY 10094, United State</div>
  </div>
  <div class="f-item" style="left:548px">
    <div class="c-ico"><svg viewBox="0 0 24 24"><path d="M6 3l3 0 2 5-2 1.5a11 11 0 0 0 5.5 5.5L16 13l5 2v3a2 2 0 0 1-2 2A16 16 0 0 1 4 5a2 2 0 0 1 2-2z" fill="#000"/></svg></div>
    <div>Phone Number<br>(+555) 014 2290</div>
  </div>
  <div class="f-item" style="left:834px">
    <div class="c-ico"><svg viewBox="0 0 24 24"><rect x="3" y="6" width="18" height="12" rx="1" fill="#000"/><polyline points="3,7 12,13 21,7" fill="none" stroke="var(--gold)" stroke-width="1.5"/></svg></div>
    <div>Email address<br>hello@velvane.com</div>
  </div>
  <div class="abs f-line" style="left:0;top:5262px;width:1200px"></div>
  <p class="abs copy">Copyright © 2025 Velvane Detailing. All Right Reserved</p>
</div>
</body>
</html>
```